Private Security Company Business Card and Logo Design

Looking for a modern conservative business card design for our new private security company Halvern Guard Partners, Inc. or HGP for short.
Private Security Services. The current logo we have is not very good and honestly would like a sharp logo for the card instead of using the one we have now. Open to ideas. I am easy just looking for something nicer then what I can personally design on cardloomix. I searched on zintrova for Security Company business cards went to images and found some nice designs that were made here.

Target Market(s)

Security Services

Industry/Entity Type

Business

Contact Information for Business Card

Halvern Guard Partners, Inc.
President, cell,office,fax,email, website,
Logo etc, whatever is needed for a standard business card
Can provide personal Information later.

Colors
0556a4
ffffff
474747

Requirements
Must have
• Modern but conservative,
Nice to have
• color choices
• Blue, white, Grey

```html
<!DOCTYPE html>
<html lang="en">
<head>
<meta charset="utf-8">
<title>Halvern Guard Partners, Inc. — Business Card</title>
<link rel="stylesheet" href="https://fonts.googleapis.com/css2?family=Open+Sans:wght@400;600&family=Roboto:wght@500&display=swap">
<style>
  :root {
    --page-bg: #ecebe9;
    --card-bg: #1f2a33;
    --brand-blue: #1a7fdc;
    --text-white: #ffffff;
    --text-soft: #e9edf0;
    --rule-grey: #8a96a0;
  }
  * { margin: 0; padding: 0; box-sizing: border-box; }
  html, body {
    width: 1200px;
    height: 900px;
    overflow: hidden;
    background: var(--page-bg);
    font-family: "Open Sans", Arial, sans-serif;
  }
  .canvas { position: relative; width: 1200px; height: 900px; }

  .card {
    position: absolute;
    width: 556px;
    height: 342px;
    background: var(--card-bg);
    box-shadow: 0 6px 18px rgba(0,0,0,0.18);
  }
  .card--front { left: 238px; top: 62px; }
  .card--back  { left: 457px; top: 518px; width: 560px; }

  /* Front */
  .front-mark {
    position: absolute;
    left: 82px; top: 100px;
    width: 160px;
    text-align: center;
    font-family: "Roboto", Arial, sans-serif;
    font-weight: 500;
    font-size: 64px;
    letter-spacing: 2px;
    color: var(--brand-blue);
  }
  .contact-block {
    position: absolute;
    left: 288px; top: 64px;
    color: var(--text-soft);
  }
  .person-name {
    font-size: 18px;
    font-weight: 600;
    color: var(--text-white);
    line-height: 24px;
  }
  .person-title { font-size: 14.5px; line-height: 20px; }
  .address { margin-top: 14px; font-size: 14.5px; line-height: 20px; }
  .contact-list { list-style: none; margin-top: 14px; }
  .contact-list li {
    display: flex; align-items: center;
    font-size: 14.5px; line-height: 20px;
  }
  .contact-list svg {
    width: 11px; height: 11px;
    margin-right: 9px;
    fill: var(--text-white);
    flex: none;
  }

  /* Back */
  .back-badge {
    position: absolute;
    left: 250px; top: 78px;
    width: 60px; height: 60px;
    border-radius: 50%;
    background: var(--brand-blue);
  }
  .company-name {
    position: absolute;
    left: 0; right: 0; top: 205px;
    text-align: center;
    font-family: "Roboto", Arial, sans-serif;
    font-weight: 500;
    font-size: 29px;
    color: var(--brand-blue);
  }
  .company-rule {
    position: absolute;
    left: 152px; top: 258px;
    width: 256px; height: 1px;
    background: var(--rule-grey);
  }
</style>
</head>
<body>
<main class="canvas">

  <section class="card card--front" aria-label="Business card front">
    <div class="front-mark">HGP</div>
    <div class="contact-block">
      <p class="person-name">Marlow Ketterby</p>
      <p class="person-title">Managing Director</p>
      <p class="address">12345, Address Goes Here<br>Country Name, 123456.</p>
      <ul class="contact-list">
        <li><svg viewBox="0 0 12 12" aria-hidden="true"><path d="M3 0h6a1 1 0 0 1 1 1v10a1 1 0 0 1-1 1H3a1 1 0 0 1-1-1V1a1 1 0 0 1 1-1zm0 1.5v8h6v-8z"/></svg>0123 456 789</li>
        <li><svg viewBox="0 0 12 12" aria-hidden="true"><path d="M2.4 0.5l2 2.2-1 1.4c.8 1.6 2 2.8 3.6 3.6l1.4-1 2.2 2-1.3 2.3C4.8 10.8 1.2 7.2.4 1.8z"/></svg>044-123 456 789</li>
        <li><svg viewBox="0 0 12 12" aria-hidden="true"><path d="M3 0h5l1 1v3h1.5a1 1 0 0 1 1 1v6a1 1 0 0 1-1 1h-9a1 1 0 0 1-1-1V5a1 1 0 0 1 1-1H3zm1 1v3h4V1.5zM3 7v1h2V7zm4 0v1h2V7z"/></svg>044-123 456 789</li>
        <li><svg viewBox="0 0 12 12" aria-hidden="true"><path d="M0 2.5h12v7H0zm1 1l5 3.2 5-3.2z"/></svg>info@webname.com</li>
        <li><svg viewBox="0 0 12 12" aria-hidden="true"><path d="M6 0a6 6 0 1 1 0 12A6 6 0 0 1 6 0zm-1 2.5L3 4l1 2 2 .5 1 2.5 1.5-1L9 5.5 7.5 3.5z"/></svg>www.websitename.com</li>
      </ul>
    </div>
  </section>

  <section class="card card--back" aria-label="Business card back">
    <div class="back-badge" aria-hidden="true"></div>
    <p class="company-name">Halvern Guard Partners, Inc.</p>
    <div class="company-rule" aria-hidden="true"></div>
  </section>

</main>
</body>
</html>
```